Business Card Design Project for - The Pellowick Greenworks Company Ltd. We are a Landscape and garden

I would like designer to use all special glosses etc so i can have a professional looking business card. The theme of the business card can reflect that of the Logo attached by MarkQuarry or your own unique ideas.. please feel free to go wild as i hope i can select a winner i like - my budget will be committed so please get involved. Good luck and thank you Lyndon

Target Market(s)

Must look Professional

General Public and Businesses including Councils, Local Government, Hospitals, Hotels, Professionals and Professional Sports People.

Industry/Entity Type

Landscape Gardening

Contact Information for Business Card

The Pellowick Greenworks Company Ltd

Mr L.R Ashcombe
Head Office - Quayfront Park Manchester
t. 0772 408 916
e. info@pellowickgreenworks.co.uk
w. www.pellowickgreenworks.co.uk

Facebook - https://www.friendpage-example.com/ThePellowickGreenworksCompany/
Twitter - https://chirpline-example.com/ThePruningCart
Instagram - https://www.snapgrid-example.com/thepellowickgreenworkscompany/?hl=en
Google+ - https://circles.searchhub-example.com/u/0/208473950162438571093
Yelp - https://www.reviewnook-example.co.uk/biz/the-pellowick-greenworks-company-manchester-4

Font styles to use
Serif
Script
Other font styles liked:
• I don't have much of an idea of font types sorry

Colors

Designer to choose colors to be used in the design.

Requirements
Must have
• A Professional look and Design
• Special effects with gloss and fading of colours possibly..
• Front and back design
Nice to have
• All special features with effects and gloss etc

```html
<!DOCTYPE html>
<html lang="en">
<head>
<meta charset="utf-8">
<title>The Pellowick Greenworks Company Ltd – Business Card</title>
<link rel="stylesheet" href="https://fonts.googleapis.com/css2?family=Cinzel:wght@400;600&family=Dancing+Script:wght@600&family=Open+Sans:wght@400;600&display=swap">
<style>
  :root {
    --page-bg: #ecebe8;
    --card-white: #ffffff;
    --leaf-light: #9fd84a;
    --leaf-mid: #4cbf3f;
    --leaf-deep: #22a84a;
    --label-green: #5aa832;
    --name-green: #2f7d22;
    --rule-green: #7cae5c;
    --text-grey: #4a4a4a;
    --soil-top: #4a2608;
    --soil-bottom: #1c0603;
    --logo-silver: #d8d4d0;
  }
  * { box-sizing: border-box; margin: 0; padding: 0; }
  html, body { width: 1200px; height: 1200px; overflow: hidden; }
  body { background: var(--page-bg); position: relative; font-family: "Open Sans", sans-serif; }

  .card {
    position: absolute; left: 150px; width: 900px; height: 514px;
    overflow: hidden; border-radius: 4px;
    box-shadow: 0 10px 30px rgba(0,0,0,.18);
  }
  .card--front { top: 56px; background: linear-gradient(125deg, #cdeaa6 0%, #eef8e2 25%, var(--card-white) 48%); }
  .card--back { top: 630px; background: linear-gradient(160deg, var(--soil-top) 0%, var(--soil-bottom) 100%); }

  /* front */
  .leaf-art {
    position: absolute; left: 70px; top: 80px; width: 360px; height: 340px;
    background: linear-gradient(135deg, rgba(159,216,74,.35) 0%, rgba(76,191,63,.55) 100%);
  }
  .details { position: absolute; left: 470px; top: 54px; width: 390px; color: var(--text-grey); }
  .label { display: flex; align-items: center; gap: 8px; color: var(--label-green); font-size: 19px; line-height: 1; }
  .label svg { width: 20px; height: 20px; fill: var(--name-green); }
  .holder-name { font-family: "Dancing Script", cursive; font-size: 46px; color: var(--name-green); line-height: 1.1; margin-top: 4px; }
  .office { font-size: 17px; margin-top: 2px; }
  .rule { height: 2px; background: var(--rule-green); margin: 12px 0 14px; }
  .value { font-size: 19px; margin: 6px 0 12px; }
  .socials { list-style: none; font-size: 14px; line-height: 1.5; }
  .socials li { display: flex; align-items: center; gap: 7px; white-space: nowrap; }
  .social-mark { width: 11px; height: 11px; background: #8a8a8a; border-radius: 2px; flex: none; }

  /* back */
  .back-art {
    position: absolute; left: 0; top: 0; width: 560px; height: 360px;
    background: linear-gradient(30deg, rgba(159,216,74,.55) 0%, rgba(34,192,74,.55) 100%);
  }
  .brand { position: absolute; right: 70px; bottom: 70px; display: flex; align-items: center; gap: 22px; color: var(--logo-silver); font-family: "Cinzel", serif; font-weight: 400; }
  .brand-dot { width: 74px; height: 74px; border-radius: 50%; background: var(--leaf-mid); flex: none; }
  .brand-name { font-size: 40px; letter-spacing: 2px; line-height: 1.05; }
  .brand-sub { font-size: 17px; letter-spacing: 4px; display: block; margin-top: 6px; }
</style>
</head>
<body>

<section class="card card--front">
  <div class="leaf-art" role="img" aria-label="Illustration of three green leaves with a glossy gradient"></div>

  <div class="details">
    <div class="label">
      <svg viewBox="0 0 20 20"><circle cx="10" cy="6" r="4.5"/><path d="M1 20c0-6 4-9 9-9s9 3 9 9z"/></svg>Name
    </div>
    <p class="holder-name">Mr L.R Ashcombe</p>
    <p class="office">Head Office - Quayfront Park Manchester</p>
    <div class="rule"></div>

    <div class="label">
      <svg viewBox="0 0 20 20"><path d="M2 7c0-3 4-5 8-5s8 2 8 5l-4 1-1-2H7L6 8zM4 10h12l2 8H2z"/></svg>Tel
    </div>
    <p class="value">0772 408 916</p>

    <div class="label">
      <svg viewBox="0 0 20 20"><circle cx="10" cy="10" r="8.5" fill="none" stroke="#2f7d22" stroke-width="2"/><path d="M2 10h16M10 2c-4 4-4 12 0 16M10 2c4 4 4 12 0 16" fill="none" stroke="#2f7d22" stroke-width="1.5"/></svg>web
    </div>
    <p class="value">www.pellowickgreenworks.co.uk</p>

    <div class="label">
      <svg viewBox="0 0 20 20"><rect x="1" y="4" width="18" height="13" rx="1"/><path d="M1 5l9 7 9-7" fill="none" stroke="#fff" stroke-width="1.5"/></svg>Email
    </div>
    <p class="value">info@pellowickgreenworks.co.uk</p>
    <div class="rule"></div>

    <ul class="socials">
      <li><span class="social-mark"></span>ThePellowickGreenworksCompany | ThePruningCart</li>
      <li><span class="social-mark"></span>thepellowickgreenworkscompany/?hl=en</li>
      <li><span class="social-mark"></span>208473950162438571093</li>
      <li><span class="social-mark"></span>the-pellowick-greenworks-company-manchester-4</li>
    </ul>
    <div class="rule"></div>
  </div>
</section>

<section class="card card--back">
  <div class="back-art" role="img" aria-label="Illustration of a large glossy green leaf across the top corner"></div>

  <div class="brand">
    <span class="brand-dot"></span>
    <p class="brand-name">THE PELLOWICK<span class="brand-sub">GREENWORKS COMPANY LTD</span></p>
  </div>
</section>

</body>
</html>
```